Business card design needed

I need a business card for my new Food & Lifestyle Coaching business - "Bloomvale Food & Lifestlye Coaching"

i already have a logo and would like to have that incorporated into the business card, obviously.

i would like a design that says "fresh" and "funky" - my target market is female, aged 20-45 so i want something that will stand out to them when they see it.

My "Company Colour" is Apple Green
Updates

Thankyou to everyone who has submitted a design for my project. At this stage i have quite a large number of designs to chose from and with only a short time until my project closes i am focusing now on chosing from those i have already shortlisted so am unfortunately not considering any new desings.

Thankyou again for your interest in my project.

Target Market(s)

Female, Health Conscious (or looking to improve their health/lifestyle), aged between 20-45

Industry/Entity Type

Business

Contact Information for Business Card

Tamsin Corley
Ph: 0417382946
Email: eatwell@marovex.com

Requirements
Must have
• Must include my existing Logo
Nice to have
• Would be nice to incoirporate and appointment card on the back

```html
<!DOCTYPE html>
<html lang="en">
<head>
<meta charset="utf-8">
<title>Bloomvale Food &amp; Lifestlye Coaching – Business Card</title>
<link rel="stylesheet" href="https://fonts.googleapis.com/css2?family=Montserrat:wght@400;600;700&display=swap">
<style>
  :root {
    --apple-green: #7dbb35;
    --apple-green-deep: #5e9e22;
    --apple-green-light: #a6d65c;
    --ink: #2e2b2c;
    --card-white: #ffffff;
    --card-white-shade: #eeeeee;
    --backdrop: #8d8d8d;
    --backdrop-dark: #5f5f5f;
  }
  * { box-sizing: border-box; margin: 0; padding: 0; }
  html, body { width: 1200px; height: 900px; overflow: hidden; }
  body {
    font-family: "Montserrat", Arial, sans-serif;
    background: radial-gradient(ellipse at 50% 40%, var(--backdrop) 0%, var(--backdrop-dark) 100%);
    position: relative;
  }
  .card {
    position: absolute;
    width: 560px;
    height: 320px;
    border-radius: 22px;
    overflow: hidden;
    box-shadow: 0 10px 24px rgba(0,0,0,0.35);
  }

  /* Front side */
  .card--front {
    left: 80px;
    top: 90px;
    background: linear-gradient(135deg, var(--apple-green-deep) 0%, var(--apple-green) 55%, var(--apple-green-light) 100%);
  }
  .card--front .motif-area {
    position: absolute;
    right: -60px;
    top: -40px;
    width: 360px;
    height: 360px;
    border-radius: 50%;
    background: radial-gradient(circle, rgba(255,255,255,0.28) 0%, rgba(255,255,255,0.12) 60%, rgba(255,255,255,0) 72%);
  }
  .card--front .brand {
    position: absolute;
    left: 0;
    right: 0;
    top: 108px;
    justify-content: center;
  }

  /* Brand lockup */
  .brand {
    display: flex;
    align-items: center;
    gap: 14px;
  }
  .brand__dot {
    width: 30px;
    height: 30px;
    border-radius: 50%;
    background: var(--card-white);
    flex: none;
  }
  .brand__name {
    color: var(--ink);
    font-weight: 600;
    line-height: 1;
  }
  .brand__title { display: block; font-size: 50px; letter-spacing: 0.5px; }
  .brand__tagline { display: block; font-size: 14px; margin-top: 8px; letter-spacing: 0.3px; }

  /* Back side */
  .card--back {
    left: 560px;
    top: 480px;
    background: linear-gradient(160deg, var(--card-white) 0%, var(--card-white) 60%, var(--card-white-shade) 100%);
  }
  .card--back .brand {
    position: absolute;
    left: 34px;
    top: 44px;
  }
  .card--back .brand__dot { background: var(--apple-green); width: 26px; height: 26px; }
  .card--back .brand__title { font-size: 40px; }
  .card--back .brand__tagline { font-size: 12px; }
  .card--back .motif-area {
    position: absolute;
    right: -40px;
    top: 30px;
    width: 280px;
    height: 290px;
    border-radius: 50% 0 0 50%;
    background: linear-gradient(135deg, var(--apple-green-light) 0%, var(--apple-green) 50%, var(--apple-green-deep) 100%);
  }
  .contact {
    position: absolute;
    left: 36px;
    bottom: 36px;
  }
  .contact__name {
    color: var(--apple-green);
    font-weight: 700;
    font-size: 26px;
    margin-bottom: 14px;
  }
  .contact__line {
    display: flex;
    align-items: center;
    gap: 12px;
    color: var(--ink);
    font-size: 19px;
    line-height: 1.45;
  }
  .contact__icon { width: 18px; height: 18px; flex: none; }
</style>
</head>
<body>

  <section class="card card--front" aria-label="Business card front">
    <div class="motif-area" role="img" aria-label="Large faint brand motif area"></div>
    <div class="brand">
      <span class="brand__dot"></span>
      <span class="brand__name">
        <span class="brand__title">Bloomvale</span>
        <span class="brand__tagline">Food &amp; Lifestlye Coaching</span>
      </span>
    </div>
  </section>

  <section class="card card--back" aria-label="Business card back">
    <div class="motif-area" role="img" aria-label="Large green brand motif area"></div>
    <div class="brand">
      <span class="brand__dot"></span>
      <span class="brand__name">
        <span class="brand__title">Bloomvale</span>
        <span class="brand__tagline">Food &amp; Lifestlye Coaching</span>
      </span>
    </div>
    <div class="contact">
      <p class="contact__name">Tamsin Corley</p>
      <p class="contact__line">
        <svg class="contact__icon" viewBox="0 0 24 24" aria-hidden="true">
          <path fill="#7dbb35" d="M6.6 10.8a15.1 15.1 0 0 0 6.6 6.6l2.2-2.2a1 1 0 0 1 1-.25 11.4 11.4 0 0 0 3.6.57 1 1 0 0 1 1 1V20a1 1 0 0 1-1 1A17 17 0 0 1 3 4a1 1 0 0 1 1-1h3.5a1 1 0 0 1 1 1c0 1.25.2 2.45.57 3.57a1 1 0 0 1-.25 1z"/>
        </svg>
        0417382946
      </p>
      <p class="contact__line">
        <svg class="contact__icon" viewBox="0 0 24 24" aria-hidden="true">
          <rect x="2" y="5" width="20" height="14" rx="1.5" fill="#7dbb35"/>
          <path d="M3 6.5l9 6.5 9-6.5" fill="none" stroke="#ffffff" stroke-width="1.6"/>
        </svg>
        eatwell@marovex.com
      </p>
    </div>
  </section>

</body>
</html>
```